Farm Entrance Sign Design for Estate - Maplewick Meadow Farm

I am seeking a sign to hang where you turn in my driveway to my farm. The name of the farm is "Maplewick Meadow Farm". The sign/logo does not need the work "Farm" in it necessarily. The sign should be simple, clean, elegant.

I will attach some basic signs that are of the quality I am seeking. I will also attach a view of the farm entrance. I do not want the sign to compete with the landscape. This is in an area of estate type farms with horses and high end homes.

We are a cattle farm. But don't necessarily have to have cow on sign.

Font styles to use
Sans Serif

Colors

Designer to choose colors to be used in the design.

Requirements
Nice to have
• I prefer a clean font...nothing fancy

```html
<!DOCTYPE html>
<html lang="en">
<head>
<meta charset="utf-8">
<title>Maplewick Meadow Farm – Entrance Sign</title>
<link href="https://fonts.googleapis.com/css2?family=Arimo:wght@600&family=Tinos&display=swap" rel="stylesheet">
<style>
  :root {
    --backdrop: #e9e7e2;
    --panel: #141414;
    --panel-edge: #262626;
    --frame-dark: #5e4e34;
    --frame-mid: #a8946c;
    --frame-light: #d9caa3;
    --lettering: #ffffff;
    --arrow-light: #e8c84a;
    --arrow-gold: #d2ad2a;
    --arrow-deep: #9c7a12;
    --berry-red: #c8161d;
    --berry-deep: #7e0b10;
  }
  * { margin: 0; padding: 0; box-sizing: border-box; }
  html, body {
    width: 800px; height: 1200px; overflow: hidden;
    background: var(--backdrop);
  }
  .canvas {
    width: 800px; height: 1200px;
    display: flex; align-items: center; justify-content: center;
  }
  .sign-frame {
    width: 640px; height: 820px;
    padding: 22px;
    background: linear-gradient(135deg, var(--frame-light), var(--frame-mid) 30%, var(--frame-dark) 55%, var(--frame-mid) 78%, var(--frame-light));
    box-shadow: inset 0 0 0 3px var(--frame-dark);
  }
  .sign-panel {
    width: 100%; height: 100%;
    background: var(--panel);
    box-shadow: inset 0 0 0 6px var(--panel-edge), inset 0 0 0 8px var(--frame-dark);
    display: flex; flex-direction: column; align-items: center;
    padding-top: 150px;
  }
  .produce-art {
    width: 240px; height: 170px;
    border-radius: 46% 46% 50% 50%;
    background: radial-gradient(ellipse at 45% 40%, var(--berry-red), var(--berry-deep) 80%);
  }
  .farm-name {
    margin-top: 24px;
    text-align: center;
    color: var(--lettering);
  }
  .farm-name__primary {
    display: block;
    font-family: "Arimo", Arial, sans-serif;
    font-weight: 600;
    font-size: 66px;
    line-height: 1;
  }
  .farm-name__secondary {
    display: block;
    font-family: "Tinos", "Times New Roman", serif;
    font-weight: 400;
    font-size: 44px;
    letter-spacing: 1px;
    line-height: 1.1;
    margin-top: 6px;
  }
  .direction-arrow {
    margin-top: 30px;
    width: 280px; height: 96px;
  }
</style>
</head>
<body>
  <main class="canvas">
    <div class="sign-frame">
      <section class="sign-panel">
        <div class="produce-art" role="img" aria-label="Photograph of a cluster of fresh red strawberries"></div>
        <h1 class="farm-name">
          <span class="farm-name__primary">MAPLEWICK</span>
          <span class="farm-name__secondary">MEADOW FARM</span>
        </h1>
        <svg class="direction-arrow" viewBox="0 0 280 96" role="img" aria-label="Turn right">
          <defs>
            <linearGradient id="arrowGold" x1="0" y1="0" x2="0" y2="1">
              <stop offset="0" style="stop-color: var(--arrow-light)"/>
              <stop offset="0.55" style="stop-color: var(--arrow-gold)"/>
              <stop offset="1" style="stop-color: var(--arrow-deep)"/>
            </linearGradient>
          </defs>
          <polygon points="0,26 170,26 170,0 280,48 170,96 170,70 0,70" fill="url(#arrowGold)"/>
        </svg>
      </section>
    </div>
  </main>
</body>
</html>
```